Turn website guide into PDF ebook

We have some guides which we would like to reformat into downloadable PDF guides. All of the content is there already, it just needs to be nicely formatted into an ebook/brochure PDF format (inkeeping with our brand style).
If you need to add any titles, images, content please feel free to, or get in touch.
Here is the first page we are looking to turn into a guide: https://www.gobrivo.com/brivo-guides/relocating-to-china/
After this we have other guides here: https://www.gobrivo.com/destinations/teaching-in-china/
(please browse around the website for more of a feeling of our brand, colors, style, target audience etc.)
Target Market(s)
20-40, those which want to travel overseas and teach English.
Look and feel

```html
<!DOCTYPE html>
<html lang="en">
<head>
<meta charset="utf-8">
<title>Olvenna – Relocating to China guide pages</title>
<link href="https://fonts.googleapis.com/css2?family=Montserrat:wght@400;500;600;700;800&family=Oswald:wght@500;600&family=Open+Sans:wght@400;600&display=swap" rel="stylesheet">
<style>
  :root {
    --board: #b3b3b3;
    --paper: #ffffff;
    --blue: #1c66b5;
    --navy: #173f7c;
    --teal: #13a095;
    --ink: #3a3a3a;
    --label: #1e1e1e;
  }
  * { margin: 0; padding: 0; box-sizing: border-box; }
  html, body { width: 954px; height: 1200px; overflow: hidden; background: var(--board); }
  .board { position: relative; width: 954px; height: 1200px; background: var(--board); font-family: "Open Sans", sans-serif; }

  .page { position: absolute; width: 376px; height: 531px; background: var(--paper); box-shadow: 0 2px 6px rgba(0,0,0,.25); overflow: hidden; }
  .page--cover { left: 54px; top: 26px; }
  .page--one { left: 505px; top: 26px; }
  .page--two { left: 54px; top: 611px; }

  .page-label { position: absolute; width: 376px; text-align: center; font-weight: 600; font-size: 14px; color: var(--label); letter-spacing: .3px; }

  /* brand */
  .brand { position: absolute; display: flex; align-items: center; gap: 7px; }
  .brand-dot { border-radius: 50%; background: var(--teal); flex: none; }
  .brand-name { font-family: "Montserrat", sans-serif; font-weight: 600; color: var(--blue); line-height: 1; }

  /* cover */
  .cover-art { position: absolute; inset: 0; }
  .cover-kicker { position: absolute; top: 427px; width: 100%; text-align: center; font-family: "Oswald", sans-serif; font-weight: 600; font-size: 25px; line-height: 30px; color: var(--navy); letter-spacing: .3px; }
  .cover-main { position: absolute; top: 458px; width: 100%; text-align: center; font-family: "Montserrat", sans-serif; font-weight: 800; font-size: 22.5px; line-height: 24px; color: var(--teal); letter-spacing: .2px; }
  .cover-rule { position: absolute; left: 126px; top: 487px; width: 124px; height: 1px; background: var(--blue); }
  .cover-url { position: absolute; left: 130px; top: 506px; width: 116px; height: 25px; background: var(--blue); border-radius: 4px 4px 0 0; color: #fff; font-size: 8px; letter-spacing: 1.4px; text-align: center; line-height: 25px; }

  /* inner pages */
  .header-rule { position: absolute; left: 0; top: 30px; width: 255px; height: 4px; border-top: 1px solid var(--blue); border-bottom: 1px solid var(--blue); }
  .section-bar { position: absolute; left: 0; width: 8px; height: 32px; background: var(--teal); }
  .section-title { position: absolute; left: 18px; font-family: "Montserrat", sans-serif; font-weight: 700; font-size: 11.3px; color: var(--teal); }
  .body-copy { position: absolute; left: 18px; width: 336px; font-size: 7.6px; line-height: 13.2px; color: var(--ink); }
  .page--two .body-copy { font-size: 7.9px; width: 334px; }
  .sub-link { position: absolute; left: 18px; font-family: "Montserrat", sans-serif; font-weight: 700; font-size: 7.8px; color: var(--blue); text-decoration: underline; }

  .steps { position: absolute; left: 18px; top: 184px; list-style: none; }
  .step { position: absolute; left: 0; display: flex; align-items: center; gap: 10px; width: 200px; }
  .step-icon { width: 38px; height: 38px; border-radius: 50%; display: flex; align-items: center; justify-content: center; }
  .step-icon.blue { background: var(--navy); border: 3px solid var(--blue); }
  .step-icon.teal { background: var(--teal); border: 3px solid #5cc7be; }
  .step-text { font-family: "Montserrat", sans-serif; font-weight: 700; font-size: 8px; color: var(--blue); }

  .kid-art { position: absolute; left: 183px; top: 270px; width: 144px; height: 228px; border-radius: 40px 40px 10px 10px; background: linear-gradient(160deg, #f6d2a3 0%, #f5c542 45%, #9fd3e0 100%); opacity: .85; }

  .footer-bar { position: absolute; left: 0; top: 507px; width: 332px; height: 19px; background: var(--blue); color: #fff; font-size: 8px; letter-spacing: 1.4px; line-height: 19px; padding-left: 19px; }
  .page-num { position: absolute; left: 347px; top: 507px; line-height: 19px; font-family: "Montserrat", sans-serif; font-weight: 700; font-size: 8px; color: var(--teal); }

  .speaker { position: absolute; width: 160px; text-align: center; }
  .speaker-icon { width: 36px; height: 36px; margin: 0 auto; border-radius: 50%; display: flex; align-items: center; justify-content: center; }
  .speaker-icon.teal { background: var(--teal); border: 3px solid #5cc7be; }
  .speaker-icon.blue { background: var(--navy); border: 3px solid var(--blue); }
  .speaker-text { margin-top: 14px; font-family: "Montserrat", sans-serif; font-weight: 700; font-size: 8px; }
  .speaker-text.teal { color: var(--teal); }
  .speaker-text.blue { color: var(--blue); }
</style>
</head>
<body>
<main class="board">

  <!-- Cover -->
  <section class="page page--cover">
    <svg class="cover-art" width="376" height="531" viewBox="0 0 376 531">
      <defs>
        <linearGradient id="streetTone" x1="0" y1="0" x2="1" y2="1">
          <stop offset="0" stop-color="#c9a98a"/>
          <stop offset=".45" stop-color="#8a7f7a"/>
          <stop offset="1" stop-color="#4d6f9a"/>
        </linearGradient>
      </defs>
      <rect x="0" y="60" width="376" height="420" fill="url(#streetTone)" role="img" aria-label="Photo of a busy Asian city street with neon signs and a traveller seen from behind"/>
      <path d="M0 66 Q188 210 376 66 L376 0 L0 0 Z" fill="#fff"/>
      <path d="M0 66 Q188 210 376 66" fill="none" stroke="var(--blue)" stroke-width="4"/>
      <path d="M0 470 Q188 320 376 470 L376 531 L0 531 Z" fill="#fff"/>
      <path d="M0 470 Q188 320 376 470" fill="none" stroke="var(--teal)" stroke-width="4"/>
    </svg>
    <div class="brand" style="left:80px; top:42px;">
      <span class="brand-dot" style="width:44px;height:44px;"></span>
      <span class="brand-name" style="font-size:38px;">Olvenna</span>
    </div>
    <div class="cover-kicker">THE COMPLETE GUIDE</div>
    <div class="cover-main">RELOCATING TO CHINA</div>
    <div class="cover-rule"></div>
    <div class="cover-url">www.olvenna.co</div>
  </section>
  <div class="page-label" style="left:54px; top:576px;">COVER PAGE</div>

  <!-- Page 01 -->
  <section class="page page--one">
    <div class="header-rule"></div>
    <div class="brand" style="left:264px; top:22px;">
      <span class="brand-dot" style="width:18px;height:18px;"></span>
      <span class="brand-name" style="font-size:15px;">Olvenna</span>
    </div>
    <div class="section-bar" style="top:70px;"></div>
    <h2 class="section-title" style="top:80px;">THESE ARE THE 5 STEPS YOU’LL NEED TO COMPLETE</h2>
    <p class="body-copy" style="top:113px;">China is a country which runs on bureaucracy – there are million rubber stamps in every government office, and if you’re hoping to teach there, you’ll need to get the right ones. Follow these steps and you’ll be fine.</p>

    <ul class="steps">
      <li class="step" style="top:0;"><span class="step-icon blue"><svg width="14" height="12" viewBox="0 0 14 12" fill="#fff"><rect x="0" y="0" width="3" height="3"/><rect x="4" y="0" width="10" height="3"/><rect x="0" y="4.5" width="3" height="3"/><rect x="4" y="4.5" width="10" height="3"/><rect x="0" y="9" width="3" height="3"/><rect x="4" y="9" width="10" height="3"/></svg></span><span class="step-text">CHECK THE VISA REQUIREMENTS</span></li>
      <li class="step" style="top:62px;"><span class="step-icon teal"><svg width="12" height="14" viewBox="0 0 12 14" fill="none" stroke="#fff" stroke-width="1.2"><path d="M1 1h7l3 3v9H1z"/><path d="M3 6h6M3 8.5h6M3 11h4"/></svg></span><span class="step-text">GET TEFL TRAINING</span></li>
      <li class="step" style="top:125px;"><span class="step-icon blue"><svg width="15" height="11" viewBox="0 0 15 11" fill="none" stroke="#fff" stroke-width="1.3"><rect x="1" y="1" width="13" height="9" rx="1"/><path d="M1 1.5l6.5 5 6.5-5"/></svg></span><span class="step-text">APPLY FOR JOBS</span></li>
      <li class="step" style="top:188px;"><span class="step-icon teal"><svg width="16" height="12" viewBox="0 0 16 12" fill="none" stroke="#fff" stroke-width="1.2"><rect x="1" y="1" width="14" height="10" rx="1"/><rect x="3" y="3.5" width="4" height="5" fill="#fff"/><path d="M9 4h4M9 6h4M9 8h3"/></svg></span><span class="step-text">GET YOUR VISA</span></li>
      <li class="step" style="top:252px;"><span class="step-icon blue"><svg width="14" height="14" viewBox="0 0 14 14" fill="#fff"><path d="M13 1L8 6l1 6-1.5 1L5.5 8 3 10.5V13L1.5 12 1 10 2 8.5 5 6 1 3.5 2 2l6 1 5-3z"/></svg></span><span class="step-text">FLY TO CHINA</span></li>
    </ul>

    <div class="kid-art" role="img" aria-label="Cartoon illustration of a child holding a giant yellow pencil"></div>

    <div class="footer-bar">www.olvenna.co</div>
    <div class="page-num">01</div>
  </section>
  <div class="page-label" style="left:505px; top:576px;">PAGE 01</div>

  <!-- Page 02 -->
  <section class="page page--two">
    <div class="header-rule"></div>
    <div class="brand" style="left:264px; top:22px;">
      <span class="brand-dot" style="width:18px;height:18px;"></span>
      <span class="brand-name" style="font-size:15px;">Olvenna</span>
    </div>
    <div class="section-bar" style="top:70px;"></div>
    <h2 class="section-title" style="top:80px;">CHECK THE VISA REQUIREMENTS</h2>
    <p class="body-copy" style="top:111px;">The first step is to check if you meet, or have the ability to meet, the visa requirements in China. It can be difficult to find a position in China if you don’t meet these requirements, as employers can face stiff fines if they’re caught hiring teachers without the correct paperwork.</p>
    <p class="body-copy" style="top:177px;">It is possible to get teaching work in China without the correct visa. Due to the high demand for teachers, some schools will still be happy to hire teachers without the appropriate visa, although we wouldn’t recommend it.</p>
    <a class="sub-link" style="top:231px;">CHINESE Z VISA REQUIREMENTS</a>
    <p class="body-copy" style="top:257px;">To legally teach English in China, you’ll need to have a type of work visa known as the “Z visa”. This is a work visa in China, and be issued for a huge range of potential work positions.</p>
    <p class="body-copy" style="top:309px;">If you’re teaching English in China, your Z visa should be for this specific purpose. To get this visa for the purpose of teaching English you’ll need to meet the following requirements:</p>

    <div class="speaker" style="left:20px; top:392px;">
      <div class="speaker-icon teal"><svg width="16" height="16" viewBox="0 0 16 16" fill="none" stroke="#fff" stroke-width="1.1"><circle cx="8" cy="8" r="6.5"/><path d="M4.5 8h7"/></svg></div>
      <div class="speaker-text teal">NATIVE ENGLISH SPEAKERS</div>
    </div>
    <div class="speaker" style="left:188px; top:392px;">
      <div class="speaker-icon blue"><svg width="16" height="16" viewBox="0 0 16 16" fill="none" stroke="#fff" stroke-width="1.1"><circle cx="8" cy="8" r="6.5"/><path d="M3.5 12.5l9-9"/></svg></div>
      <div class="speaker-text blue">NON-NATIVE ENGLISH SPEAKERS</div>
    </div>

    <div class="footer-bar">www.olvenna.co</div>
    <div class="page-num">02</div>
  </section>
  <div class="page-label" style="left:54px; top:1161px;">PAGE 02</div>

  <!-- Brand showcase -->
  <div class="brand" style="left:548px; top:840px; gap:10px;">
    <span class="brand-dot" style="width:70px;height:70px;"></span>
    <span class="brand-name" style="font-size:52px;">Olvenna</span>
  </div>

</main>
</body>
</html>
```